Creative UI design for web application

I need a new UI design for my web application. It will be used by small and micro business owners to plan & implement growth tactics.

I've attached the current design (which I'm open to be changed) - but in particular I need to design the centre of the screen, where the work actually happens.

There needs to be place for a title (YOUR BUSINESS) and description (say 1-2 paragraphs of text) - and am happy to include icons or imagery where makes sense. It may make sense for the user to be able to upload their business logo and name, for example.

This screen will be used by the business owner to understand the real value they offer potential customers and their point of difference - why they exist and why potential customers should care.

They'll use the information they put into this screen to plan things like their messaging.

Following that, there needs to be 2 sections in the dashboard.

The first section is titled "WHO YOU ARE"

The first section will include a number of boxes that the user can input information into, as follows:

- Logo
- Business name
- Business tag line
- Business vision
- Business bio
- Brand colours (these should end up as swatches based on the colour code they enter) - the colour code for each colour swatch should also be visible.
- Key competitors
- SWOT analysis (boxes to enter their strengths, weaknesses, opportunities and threats).

The second section is titled "WHY YOU EXIST"

The second section will include a number of boxes that the user can input information (text) into, as follows:

- Who are your ideal customers?
- What problem are you trying to solve for them?
- What pain points will this remove for them?
- How do you solve it?
- How else could this problem be solved?
- Who offers these other solutions?
- Why is your solution better?
- How much does your solution cost?
- What value are you providing to justify this cost?
- How will this make their life/job easier/better?

They should be able to write a decent amount of information in the boxes.

There should ideally be a place for a description for each of these text fields (for both section 1 & 2) as well so I can give them a little bit more direction around what to put in the box. Alternatively there could be a little icon (say a question mark or "i") that they could click on to view instructions. The instructions will be around 2-4 sentences long for each text field.

You have 2 options:

a) This all needs to appear on the one screen, and the navigation needs to be visible (as per the example attached but feel free to recreate this navigation)

Note: the page can scroll below the fold - but please provide the design for the full length of the page.

b) Potentially the 2 sections could actually be in 2 different items in the menu - YOUR BUSINESS and YOUR VALUE (which would sit next to YOUR BUSINESS and before YOUR CUSTOMER in the screenshot provided). feel free to design them as 2 separate screens if you prefer.

I have attached a screenshot of the app as it stands today (screen shot 2017) which would still exist in the new design but under a different section (the learn section from the plan2 mockup attached)

I have mocked up how this new screen could look if broken into 2 and that's also attached. If you can make this come to life - and look more engaging that would be helpful! :)

Target Market(s)

Small and micro business owners

Industry/Entity Type

Marketing

Number of Pages Required

1 page

Font styles to use
Sans Serif
Other font styles liked:
• Montserrat

Colors
87cfc6
d2a4cc
ffffff
85cae6
e8e8e8
5c5c5c

Requirements
Must have
• Use of my brand colours: #cc8eb2, #76d6c8, #68c7ff as well as white and #595959. Must be visually pleasing / engaging, designed for desktop (as it's a desktop application), really easy to use / navigate.
• Use font Montserrat light & Montserrat Regular or Bold. Mostly should be Montserrat light.
Nice to have
• Would be nice to see how this would look on mobile (as the application is responsive) but this is not mandatory.
Should not have
• Should not look too corporate or dry.

```html
<!DOCTYPE html>
<html lang="en">
<head>
<meta charset="utf-8">
<title>Greenlift – Your Business</title>
<link href="https://fonts.googleapis.com/css2?family=Montserrat:wght@300;400;500&display=swap" rel="stylesheet">
<style>
:root{
  --bar:#3a3a3a;
  --footer:#2e2e2e;
  --pink:#d18fb7;
  --pink-dark:#b9779e;
  --heading:#c07aa6;
  --teal:#76d6c8;
  --teal-text:#6fd1c3;
  --panel:#f2f2f2;
  --field-border:#dadada;
  --text:#4a4a4a;
  --muted:#5c5c5c;
  --white:#ffffff;
  --icon:#6a6a6a;
}
*{box-sizing:border-box;margin:0;padding:0}
html,body{width:1200px;height:2305px;overflow:hidden}
body{position:relative;background:var(--white);font-family:'Montserrat',sans-serif;font-weight:300;color:var(--text)}

/* top bar */
.top-bar{position:absolute;left:0;top:0;width:1200px;height:63px;background:var(--bar)}
.brand{position:absolute;left:132px;top:21px;display:flex;align-items:center;gap:8px;color:var(--white);font-size:19px;font-weight:400;letter-spacing:.5px}
.brand-dot{width:9px;height:9px;border-radius:50%;background:var(--white)}
.main-nav{position:absolute;top:0;height:63px;left:0;width:1200px}
.main-nav a{position:absolute;top:24px;display:flex;align-items:center;gap:6px;font-size:12px;color:var(--white);text-decoration:none;font-weight:400}
.main-nav a.is-active{color:var(--teal-text)}
.main-nav svg{width:11px;height:11px}

/* section tabs */
.section-tabs{position:absolute;left:0;top:63px;width:1200px;height:41px;background:var(--pink)}
.section-tabs a{position:absolute;top:0;height:41px;line-height:41px;font-size:13px;color:var(--white);text-decoration:none;font-weight:400}
.section-tabs a.is-active{background:var(--pink-dark);padding:0 14px}

/* business profile card */
.profile-card{position:absolute;left:132px;top:135px;width:934px;height:377px;background:var(--panel)}
.profile-head{height:114px;border-bottom:1px solid #dcdcdc;position:relative}
.profile-mark{position:absolute;left:23px;top:27px;width:62px;height:62px;border-radius:50%;background:#111}
.profile-name{position:absolute;left:106px;top:38px;font-size:13px;font-weight:400;color:#333;letter-spacing:.3px}
.profile-name span{display:block;font-size:13px;font-weight:300;margin-top:2px;margin-left:4px}
.profile-contact{position:absolute;left:578px;top:50px;display:flex;align-items:center;gap:6px;font-size:13px;font-weight:400;color:#333}
.profile-social{position:absolute;top:53px;width:10px;height:10px;border-radius:50%}
.photo{position:absolute;left:23px;top:143px;width:240px;height:200px;background:linear-gradient(135deg,#5a3b33 0%,#b07c6c 45%,#d8c7be 100%)}
.about{position:absolute;left:278px;top:142px;width:633px}
.about h3{font-size:11px;font-weight:400;color:#333;margin-bottom:6px}
.about p{font-size:9.6px;line-height:20.7px;color:#333;font-weight:400;margin-bottom:20px}

/* form panels */
.panel{position:absolute;left:132px;width:934px;background:var(--panel)}
.panel-who{top:544px;height:656px}
.panel-why{top:1235px;height:824px}
.panel h2{position:absolute;left:23px;font-size:25px;font-weight:300;color:var(--heading)}
.field{position:absolute;background:var(--white);border:1px solid var(--field-border);font-size:12px;font-weight:400;color:#444}
.field-label{position:absolute;left:14px;top:12px}
.field-tools{position:absolute;right:14px;top:12px;display:flex;gap:6px}
.field-tools svg{width:12px;height:12px}
.swatches{position:absolute;left:120px;top:7px;display:flex;gap:5px}
.swatch{width:80px;height:26px;line-height:26px;text-align:center;font-size:9.5px;font-weight:400}
.subheading{position:absolute;left:23px;top:324px;font-size:15px;font-weight:400;color:#333}

/* actions */
.save-button{position:absolute;left:519px;top:2096px;width:160px;height:47px;background:var(--teal);color:#2f3d3b;font-size:14px;font-weight:400;border:0;font-family:'Montserrat',sans-serif}

.site-footer{position:absolute;left:0;top:2223px;width:1200px;height:82px;background:var(--footer);color:#cfcfcf;font-size:10px;font-weight:400;text-align:center;line-height:82px}
</style>
</head>
<body>

<header class="top-bar">
  <div class="brand"><span>Greenlift</span><span class="brand-dot"></span></div>
  <nav class="main-nav">
    <a class="is-active" style="left:592px"><svg viewBox="0 0 12 12"><rect x="2" y="1" width="8" height="10" fill="currentColor"/></svg>Plan</a>
    <a style="left:682px"><svg viewBox="0 0 12 12"><rect x="2" y="1" width="8" height="10" rx="1" fill="currentColor"/></svg>Learn</a>
    <a style="left:777px"><svg viewBox="0 0 12 12"><path d="M6 1a3.5 3.5 0 0 1 3.5 3.5V8l1.5 1.5H1L2.5 8V4.5A3.5 3.5 0 0 1 6 1zM4.5 10.5h3a1.5 1.5 0 0 1-3 0z" fill="currentColor"/></svg>Remember</a>
    <a style="left:902px"><svg viewBox="0 0 12 12"><circle cx="6" cy="3.5" r="2.5" fill="currentColor"/><path d="M1 11a5 4 0 0 1 10 0z" fill="currentColor"/></svg>My Profile</a>
    <a style="left:1011px"><svg viewBox="0 0 12 12"><path d="M1 6h6M5 3.5 7.5 6 5 8.5" stroke="currentColor" stroke-width="1.6" fill="none"/><path d="M6 1.5h4.5v9H6" stroke="currentColor" stroke-width="1.4" fill="none"/></svg>Logout</a>
  </nav>
</header>

<nav class="section-tabs">
  <a class="is-active" style="left:132px">Your Business</a>
  <a style="left:266px">Your Value</a>
  <a style="left:366px">Your Product</a>
  <a style="left:482px">Your Customer</a>
  <a style="left:609px">Your Goals</a>
  <a style="left:709px">Your Plan</a>
</nav>

<section class="profile-card">
  <div class="profile-head">
    <div class="profile-mark"></div>
    <div class="profile-name">LENA MARSH MAKEUP<span>lenamarshmakeup.com</span></div>
    <div class="profile-contact"><svg width="11" height="9" viewBox="0 0 11 9"><rect width="11" height="9" fill="#333"/><path d="M0 0l5.5 4.5L11 0" stroke="#f2f2f2" fill="none"/></svg>hello@lenamarshmakeup.com</div>
    <span class="profile-social" style="left:804px;background:#3b5998"></span>
    <span class="profile-social" style="left:836px;background:#1da1f2"></span>
    <span class="profile-social" style="left:867px;background:#dd4b39"></span>
    <span class="profile-social" style="left:900px;background:#3f729b"></span>
  </div>
  <div class="photo" role="img" aria-label="Photo of a makeup artist styling a client's hair"></div>
  <div class="about">
    <h3>Description</h3>
    <p>Cras viverra nisl at viverra fringilla. Curabitur finibus lacinia pulvinar. Proin at quam consectetur augue fringilla interdum. Cras mollis commodo vestibulum. Curabitur tincidunt erat ac libero consectetur, at interdum libero imperdiet. Quisque sed neque tempor, porta quam ac, imperdiet nunc. Sed sit amet nisi sit amet nulla finibus porta vel quis purus. Curabitur congue risus nunc, vitae porta dui efficitur id. Mauris varius consectetur metus nec pharetra.</p>
    <p>Morbi quis pretium ligula. Aliquam suscipit et magna sed tincidunt. Cras tortor orci, venenatis et nunc at, semper vestibulum leo. Morbi non sem sapien. Maecenas eleifend pellentesque fermentum. Aliquam mollis lorem eu erat laoreet, eu fringilla risus tincidunt. Aenean ac tempus nisi. Nunc sollicitudin quam at diam blandit maximus. Curabitur sodales maximus rhoncus. Nunc eget enim felis. Nulla ullamcorper feugiat vestibulum.</p>
  </div>
</section>

<svg width="0" height="0" style="position:absolute">
  <defs>
    <symbol id="info" viewBox="0 0 12 12"><circle cx="6" cy="6" r="6" fill="#6a6a6a"/><rect x="5.2" y="2.5" width="1.6" height="4.5" fill="#fff"/><rect x="5.2" y="8" width="1.6" height="1.6" fill="#fff"/></symbol>
    <symbol id="add" viewBox="0 0 12 12"><circle cx="6" cy="6" r="6" fill="#6a6a6a"/><path d="M6 3v6M3 6h6" stroke="#fff" stroke-width="1.6"/></symbol>
    <symbol id="folder" viewBox="0 0 12 12"><path d="M0 2h4.5l1 1.3H12V11H0z" fill="#6a6a6a"/></symbol>
  </defs>
</svg>

<section class="panel panel-who">
  <h2 style="top:44px">Who You Are</h2>
  <div class="field" style="left:23px;top:78px;width:218px;height:40px"><span class="field-label">Logo</span><span class="field-tools"><svg><use href="#folder"/></svg><svg><use href="#info"/></svg></span></div>
  <div class="field" style="left:247px;top:78px;width:217px;height:40px"><span class="field-label">Business name</span><span class="field-tools"><svg><use href="#info"/></svg></span></div>
  <div class="field" style="left:470px;top:78px;width:217px;height:40px"><span class="field-label">Business tag line</span><span class="field-tools"><svg><use href="#info"/></svg></span></div>
  <div class="field" style="left:695px;top:78px;width:216px;height:40px"><span class="field-label">Business vision</span><span class="field-tools"><svg><use href="#info"/></svg></span></div>
  <div class="field" style="left:23px;top:126px;width:888px;height:40px"><span class="field-label">Business bio</span><span class="field-tools"><svg><use href="#info"/></svg></span></div>
  <div class="field" style="left:23px;top:174px;width:888px;height:40px"><span class="field-label">Brand colours</span>
    <div class="swatches">
      <span class="swatch" style="background:#000;color:#fff">#000000</span>
      <span class="swatch" style="background:#fff;color:#333;border:1px solid #ddd">#ffffff</span>
      <span class="swatch" style="background:#e1e1e1;color:#333">#e1e1e1</span>
      <span class="swatch" style="background:#c2c2c2;color:#333">#c2c2c2</span>
      <span class="swatch" style="background:#a1a1a1;color:#fff">#a1a1a1</span>
      <span class="swatch" style="background:#464646;color:#fff">#464646</span>
    </div>
    <span class="field-tools"><svg><use href="#add"/></svg><svg><use href="#info"/></svg></span></div>
  <div class="field" style="left:23px;top:223px;width:888px;height:63px"><span class="field-label">Key competitors</span><span class="field-tools"><svg><use href="#add"/></svg><svg><use href="#info"/></svg></span></div>
  <div class="subheading">SWOT analysis</div>
  <div class="field" style="left:23px;top:343px;width:888px;height:63px"><span class="field-label">Strengths</span><span class="field-tools"><svg><use href="#info"/></svg></span></div>
  <div class="field" style="left:23px;top:415px;width:888px;height:63px"><span class="field-label">Weaknesses</span><span class="field-tools"><svg><use href="#info"/></svg></span></div>
  <div class="field" style="left:23px;top:487px;width:888px;height:63px"><span class="field-label">Opportunities</span><span class="field-tools"><svg><use href="#info"/></svg></span></div>
  <div class="field" style="left:23px;top:560px;width:888px;height:63px"><span class="field-label">Threats</span><span class="field-tools"><svg><use href="#info"/></svg></span></div>
</section>

<section class="panel panel-why">
  <h2 style="top:46px">Why You Exist</h2>
  <div class="field" style="left:23px;top:79px;width:888px;height:63px"><span class="field-label">Who are your ideal customers?</span><span class="field-tools"><svg><use href="#info"/></svg></span></div>
  <div class="field" style="left:23px;top:151px;width:888px;height:63px"><span class="field-label">What problem are you trying to solve for them?</span><span class="field-tools"><svg><use href="#info"/></svg></span></div>
  <div class="field" style="left:23px;top:223px;width:888px;height:63px"><span class="field-label">What pain points will this remove for them?</span><span class="field-tools"><svg><use href="#info"/></svg></span></div>
  <div class="field" style="left:23px;top:296px;width:888px;height:63px"><span class="field-label">How do you solve it?</span><span class="field-tools"><svg><use href="#info"/></svg></span></div>
  <div class="field" style="left:23px;top:368px;width:888px;height:63px"><span class="field-label">How else could this problem be solved?</span><span class="field-tools"><svg><use href="#info"/></svg></span></div>
  <div class="field" style="left:23px;top:440px;width:888px;height:63px"><span class="field-label">Who offers these other solutions?</span><span class="field-tools"><svg><use href="#info"/></svg></span></div>
  <div class="field" style="left:23px;top:512px;width:888px;height:63px"><span class="field-label">Why is your solution better?</span><span class="field-tools"><svg><use href="#info"/></svg></span></div>
  <div class="field" style="left:23px;top:584px;width:888px;height:63px"><span class="field-label">How much does your solution cost?</span><span class="field-tools"><svg><use href="#info"/></svg></span></div>
  <div class="field" style="left:23px;top:657px;width:888px;height:63px"><span class="field-label">What value are you providing to justify this cost?</span><span class="field-tools"><svg><use href="#info"/></svg></span></div>
  <div class="field" style="left:23px;top:729px;width:888px;height:63px"><span class="field-label">How will this make their life/job easier/better?</span><span class="field-tools"><svg><use href="#info"/></svg></span></div>
</section>

<button class="save-button">Save Changes</button>

<footer class="site-footer">Copyright © 2017 Greenlift. Al rights reserved.</footer>

</body>
</html>
```